Velvet Crest Car Detailing Brochure

I would like a trifold brochure designed for my car detailing business. The background has to be full black or mostly black with some designing using only colors present in our logo.

Front page must have our logo and name, list of services, a photo and mybe our phone number but no long text.

Inside I want to present each service one by one with its description and a photo representing/showing each service. (I will provide the text below). For photos, use stock photos and I will add come of mines already too.

On the back of the brochure I want to have contact & info: phone number, opening hours, address, website, Instagram.

Outside left I want the text About us and photo/design.

I want the brochure to be neat, professional, easy to read, but at the same time not too boring.

Text:
1. About us
a. the ultimate destination for car care in Geneva. We provide personalized, detail-oriented services that bring out the best in your car. With our expert techniques and dedicated approach, we ensure that your car receives the utmost care and attention. Experience a place where passion meets precision and let us create an exceptional car care experience designed just for you.
2. Services:

DETAILING & HAND WASH

• Comprehensive exterior & interior care
• Personalisation and tailored cleaning packages
• Decontamination
• Premium products
• Attention to detail for a perfect finish

POLISHING

• Eliminates scratches, holograms
• Revives and protects paint
• Ensures lasting gloss
• Enhances paint life
• Preserves car’s value and beauty

CERAMIC TREATMENT

• Durable paint protection
• Water-repellent (hydrophobic) effect
• Easier cleaning, enhanced shine
• Long-term surface safeguarding
• Shields against environmental impacts

DRY ICE WASH

• Innovative, waterless method
• Safe for all car parts
• Deep cleans, removes odors
• Allergen-free, antibacterial
• Gentle, effective
• Advanced cleaning technology

COVERING

• Personalized vehicle styling
• More than 150 colours available
• Clean cut without using a cutter
• High-quality, durable materials
• Custom designs available

PROTECTION FILM

• Invisible, durable shield
• Self-healing technology
• 10-year warranty by QR VONT

DETAILING BOUTIQUE

• Premium brands available
• Buy on site during your visit
• Marble Harbour, Zeb Autos, DRUP Polaro
• Essential for at-home car care
• Perfect for quick touch-ups
(for these three brands you can put their logos

Target Market(s)

Our target market includes car owners of all price ranges, with a special focus on those who are passionate about their vehicles. We cater to clients who value excellent service and results, and seek to maintain their cars in pristine condition.

Industry/Entity Type

Automobile / Car detailing

Colors

Designer to choose colors to be used in the design.

Requirements
Must have
• Brand Consistency: The brochure must adhere to our brand colors and style, particularly utilizing the colors present in our logo. Trifold Layout: The design must be specifically tailored for a trifold brochure format. Legibility: Text must be easy to read against the mostly black background, with appropriate font size and style. Professional Look and Feel: The overall design must convey professionalism while being engaging and not overly complex. Photo representation: each service description should have a phot presenting it.
Should not have
• Overcrowded Design: Avoid cluttering with too much text or too many images. The layout should be clean and easy to navigate. Cartoonish Fonts or Graphics: Avoid using unprofessional or casual fonts and graphics that do not align with the upscale and professional image of our business. Distracting Backgrounds: The background should complement and not overpower the content. Stick to the theme of mostly black with design elements from our logo.

```html
<!DOCTYPE html>
<html lang="en">
<head>
<meta charset="utf-8">
<title>Velvet Crest Car Detailing – Trifold Brochure</title>
<link href="https://fonts.googleapis.com/css2?family=Poppins:wght@300;400;500;600;700&display=swap" rel="stylesheet">
<style>
  :root{
    --page:#e9e9eb;
    --ink:#0b0b0c;
    --white:#ffffff;
    --magenta:#e11fd2;
    --violet:#8b3ee6;
    --blue:#3796e8;
    --muted:#d9d9de;
  }
  html,body{margin:0;padding:0;width:1200px;height:951px;overflow:hidden;background:var(--page);}
  body{position:relative;font-family:'Poppins',sans-serif;}
  .spread{position:absolute;left:275px;width:650px;height:460px;display:block;}
  .spread--outside{top:10px;}
  .spread--inside{top:481px;}
  .about-title{font:700 30px 'Poppins',sans-serif;}
  .about-copy{font:400 12.5px 'Poppins',sans-serif;fill:var(--white);}
  .brand-name{font:300 21px 'Poppins',sans-serif;fill:var(--white);letter-spacing:.5px;}
  .phone-number{font:400 22px 'Poppins',sans-serif;fill:var(--white);}
  .touch-title{font:500 18px 'Poppins',sans-serif;fill:var(--white);}
  .contact-line{font:400 12px 'Poppins',sans-serif;fill:var(--white);}
  .service-item{font:600 13px 'Poppins',sans-serif;fill:var(--white);}
  .svc-title{font:700 19px 'Poppins',sans-serif;fill:var(--white);}
  .bullet{font:400 10.3px 'Poppins',sans-serif;fill:var(--white);}
  .pill{fill:url(#pillGrad);}
  .ring{stroke:url(#ringGrad);stroke-width:5;}
  .icon-line{fill:none;stroke:var(--white);stroke-width:1.6;stroke-linecap:round;stroke-linejoin:round;}
</style>
</head>
<body>

<!-- OUTSIDE SPREAD: about / back / cover -->
<svg class="spread spread--outside" viewBox="0 0 938 663" xmlns="http://www.w3.org/2000/svg" aria-label="Brochure outside spread">
  <defs>
    <linearGradient id="brandGrad" x1="0" y1="0" x2="1" y2="0">
      <stop offset="0" stop-color="#e11fd2"/><stop offset="1" stop-color="#3796e8"/>
    </linearGradient>
    <linearGradient id="aboutGrad" gradientUnits="userSpaceOnUse" x1="56" y1="0" x2="205" y2="0">
      <stop offset="0" stop-color="#e11fd2"/><stop offset="1" stop-color="#4a7ff0"/>
    </linearGradient>
    <linearGradient id="pillGrad" x1="0" y1="0" x2="1" y2="0">
      <stop offset="0" stop-color="#c93de0"/><stop offset=".25" stop-color="#3a8fe8"/><stop offset="1" stop-color="#2f9ae6"/>
    </linearGradient>
    <linearGradient id="ringGrad" x1="0" y1="0" x2="1" y2="1">
      <stop offset="0" stop-color="#3796e8"/><stop offset="1" stop-color="#e11fd2"/>
    </linearGradient>
    <linearGradient id="purpleFade" x1="0" y1="1" x2="1" y2="0">
      <stop offset="0" stop-color="#b44cf0"/><stop offset="1" stop-color="#4a1a78"/>
    </linearGradient>
    <linearGradient id="blueCarTone" x1="0" y1="0" x2="1" y2="1">
      <stop offset="0" stop-color="#1a1d2a"/><stop offset=".5" stop-color="#1d3aa8"/><stop offset="1" stop-color="#0c1440"/>
    </linearGradient>
    <linearGradient id="interiorTone" x1="0" y1="0" x2="1" y2="1">
      <stop offset="0" stop-color="#3a3a3c"/><stop offset="1" stop-color="#111112"/>
    </linearGradient>
    <linearGradient id="redCarTone" x1="0" y1="0" x2="1" y2="1">
      <stop offset="0" stop-color="#5a5c62"/><stop offset=".45" stop-color="#c2141e"/><stop offset="1" stop-color="#5e0409"/>
    </linearGradient>
    <radialGradient id="thumbTone" cx=".4" cy=".4" r=".7">
      <stop offset="0" stop-color="#b9bcc4"/><stop offset="1" stop-color="#3c3e46"/>
    </radialGradient>
    <pattern id="stripes" width="38" height="38" patternUnits="userSpaceOnUse" patternTransform="rotate(-40)">
      <rect width="38" height="38" fill="#0d0d0e"/>
      <rect width="19" height="38" fill="#161617"/>
    </pattern>
    <symbol id="tick" viewBox="0 0 12 12">
      <circle cx="6" cy="6" r="5" fill="none" stroke="#b84cf0" stroke-width="1"/>
      <path d="M3.4 6.1 5.3 8 9.6 3.2" fill="none" stroke="#e11fd2" stroke-width="1.3" stroke-linecap="round" stroke-linejoin="round"/>
    </symbol>
  </defs>

  <rect class="backdrop" width="938" height="663" fill="url(#stripes)"/>

  <!-- hero photo band -->
  <g role="img" aria-label="Photo: technician machine-polishing the bonnet of a blue car">
    <polygon points="305,0 660,0 938,300 938,349 668,349" fill="url(#blueCarTone)"/>
  </g>
  <polygon class="accent-stripe" points="273,0 305,0 668,349 636,349" fill="#d81fd0"/>
  <polygon class="logo-field" points="660,0 938,0 938,300" fill="#050505"/>

  <!-- brand -->
  <g class="brand">
    <circle cx="860" cy="70" r="34" fill="none" stroke="#b84cf0" stroke-width="3"/>
    <text class="brand-name" x="860" y="138" text-anchor="middle">VELVET</text>
    <text class="brand-name" x="860" y="162" text-anchor="middle">CREST</text>
  </g>

  <!-- phone band -->
  <polygon class="phone-band" points="628,349 938,349 938,412 690,412" fill="url(#brandGrad)"/>
  <circle cx="746" cy="380" r="17" fill="#ffffff"/>
  <path d="M740 372c1-1 2-1 3 0l2 3c.5 1 0 2-1 2.5 1 2 2.5 3.5 4.5 4.5.5-1 1.5-1.5 2.5-1l3 2c1 1 1 2 0 3-2 2-5 1.5-9-2s-6-8-5-12z" fill="#b84cf0"/>
  <text class="phone-number" x="770" y="389">0198-765-432</text>

  <!-- about -->
  <text class="about-title" x="56" y="95" fill="url(#aboutGrad)">ABOUT US</text>
  <text class="about-copy" x="45">
    <tspan x="45" y="146">The ultimate destination for car care</tspan>
    <tspan x="45" y="160.7">in Geneva. We provide personalized,</tspan>
    <tspan x="45" y="175.4">detail-oriented services that bring out</tspan>
    <tspan x="45" y="190.1">the best in your car. With our expert</tspan>
    <tspan x="45" y="204.8">techniques and dedicated approach,</tspan>
    <tspan x="45" y="219.5">we ensure that your car receives the</tspan>
    <tspan x="45" y="234.2">utmost care and attention. Experience</tspan>
    <tspan x="45" y="248.9">a place where passion meets</tspan>
    <tspan x="45" y="263.6">precision and let us create an</tspan>
    <tspan x="45" y="278.3">exceptional car care experience</tspan>
    <tspan x="45" y="293">designed just for you.</tspan>
  </text>

  <!-- bottom-left photo -->
  <polygon class="accent-stripe" points="0,372 262,372 316,426 316,450 255,390 0,390" fill="url(#brandGrad)"/>
  <g role="img" aria-label="Photo: gloved hand cleaning a car interior air vent with a detailing brush">
    <polygon points="0,390 255,390 316,450 316,663 0,663" fill="url(#interiorTone)"/>
  </g>

  <!-- contact -->
  <text class="touch-title" x="405" y="381">Get in Touch</text>
  <g class="contact">
    <circle cx="414" cy="425" r="15" fill="#8b3ee6"/>
    <path class="icon-line" d="M409 419c1-1 2-1 2.5 0l1.5 2c.3.8 0 1.5-.8 2 .8 1.5 2 2.7 3.5 3.5.5-.8 1.2-1.1 2-.8l2 1.5c1 .5 1 1.5 0 2.5-1.5 1.5-4 1-7-1.5s-5-6-3.7-9.2z"/>
    <text class="contact-line" x="438" y="430">022 843 19 07</text>

    <circle cx="414" cy="466" r="15" fill="#8b3ee6"/>
    <path class="icon-line" d="M414 475s-6-6-6-10a6 6 0 0 1 12 0c0 4-6 10-6 10z"/><circle class="icon-line" cx="414" cy="465" r="2"/>
    <text class="contact-line" x="438" y="471">Yor Address here</text>

    <circle cx="414" cy="512" r="15" fill="#8b3ee6"/>
    <circle class="icon-line" cx="414" cy="512" r="7"/><path class="icon-line" d="M414 507.5v4.5l3 2"/>
    <text class="contact-line" x="438" y="513">Monday - Friday</text>
    <text class="contact-line" x="438" y="526">10 AM - 5 PM</text>

    <circle cx="414" cy="559" r="15" fill="#8b3ee6"/>
    <circle class="icon-line" cx="414" cy="559" r="7"/><ellipse class="icon-line" cx="414" cy="559" rx="3" ry="7"/><path class="icon-line" d="M407 559h14"/>
    <text class="contact-line" x="438" y="564">www.velvetcrest.com</text>

    <circle cx="414" cy="606" r="15" fill="#8b3ee6"/>
    <text class="contact-line" x="438" y="611">@velvetcrest</text>
  </g>

  <!-- service list -->
  <g class="service-list">
    <use href="#tick" x="666" y="459" width="14" height="14"/><text class="service-item" x="692" y="472">DETAILING &amp; HAND WASH</text>
    <use href="#tick" x="666" y="482" width="14" height="14"/><text class="service-item" x="692" y="495">POLISHING</text>
    <use href="#tick" x="666" y="506" width="14" height="14"/><text class="service-item" x="692" y="519">CERAMIC TREATMENT</text>
    <use href="#tick" x="666" y="529" width="14" height="14"/><text class="service-item" x="692" y="542">DRY ICE WASH</text>
    <use href="#tick" x="666" y="552" width="14" height="14"/><text class="service-item" x="692" y="565">COVERING</text>
    <use href="#tick" x="666" y="575" width="14" height="14"/><text class="service-item" x="692" y="588">PROTECTION FILM</text>
    <use href="#tick" x="666" y="598" width="14" height="14"/><text class="service-item" x="692" y="611">DETAILING BOUTIQUE</text>
  </g>
</svg>

<!-- INSIDE SPREAD: services -->
<svg class="spread spread--inside" viewBox="0 0 938 663" xmlns="http://www.w3.org/2000/svg" aria-label="Brochure inside spread">
  <rect class="backdrop" width="938" height="663" fill="url(#stripes)"/>

  <g role="img" aria-label="Photo: close-up of a car wheel washed in purple light">
    <polygon points="0,410 185,663 0,663" fill="url(#purpleFade)" opacity=".85"/>
  </g>

  <polygon class="accent-stripe" points="690,477 938,477 938,497 690,497 627,560 627,540" fill="url(#brandGrad)"/>
  <g role="img" aria-label="Photo: gloved hand polishing the glossy red bonnet of a car">
    <polygon points="690,497 938,497 938,663 627,663 627,560" fill="url(#redCarTone)"/>
  </g>

  <!-- Detailing & hand wash -->
  <g class="service-card" transform="translate(71,69)">
    <rect class="pill" x="-10" y="-26" width="210" height="52" rx="8"/>
    <g role="img" aria-label="Photo: hand washing a car headlight"><circle class="ring" r="34" fill="url(#thumbTone)"/></g>
    <text class="svc-title" x="56" y="-3">DETAILING &amp;</text>
    <text class="svc-title" x="56" y="19">HAND WASH</text>
    <use href="#tick" x="-30" y="55" width="11" height="11"/><text class="bullet" x="-6" y="64">Comprehensive exterior &amp; interior care</text>
    <use href="#tick" x="-30" y="72.5" width="11" height="11"/><text class="bullet" x="-6" y="81.5">Personalisation and tailored cleaning packages</text>
    <use href="#tick" x="-30" y="90" width="11" height="11"/><text class="bullet" x="-6" y="99">Decontamination</text>
    <use href="#tick" x="-30" y="107.5" width="11" height="11"/><text class="bullet" x="-6" y="116.5">Premium products</text>
    <use href="#tick" x="-30" y="125" width="11" height="11"/><text class="bullet" x="-6" y="134">Attention to detail for a perfect finish</text>
  </g>

  <!-- Ceramic treatment -->
  <g class="service-card" transform="translate(374,69)">
    <rect class="pill" x="-10" y="-26" width="210" height="52" rx="8"/>
    <g role="img" aria-label="Photo: ceramic coating applied to a car engine bay"><circle class="ring" r="34" fill="url(#thumbTone)"/></g>
    <text class="svc-title" x="56" y="-3">CERAMIC</text>
    <text class="svc-title" x="56" y="19">TREATMENT</text>
    <use href="#tick" x="-30" y="55" width="11" height="11"/><text class="bullet" x="-6" y="64">Durable paint protection</text>
    <use href="#tick" x="-30" y="72.5" width="11" height="11"/><text class="bullet" x="-6" y="81.5">Water-repellent (hydrophobic) effect</text>
    <use href="#tick" x="-30" y="90" width="11" height="11"/><text class="bullet" x="-6" y="99">Easier cleaning, enhanced shine</text>
    <use href="#tick" x="-30" y="107.5" width="11" height="11"/><text class="bullet" x="-6" y="116.5">Long-term surface safeguarding</text>
    <use href="#tick" x="-30" y="125" width="11" height="11"/><text class="bullet" x="-6" y="134">Shields against environmental impacts</text>
  </g>

  <!-- Protection film -->
  <g class="service-card" transform="translate(680,69)">
    <rect class="pill" x="-10" y="-26" width="210" height="52" rx="8"/>
    <g role="img" aria-label="Photo: protection film applied over a headlight"><circle class="ring" r="34" fill="url(#thumbTone)"/></g>
    <text class="svc-title" x="56" y="-3">PROTECTION</text>
    <text class="svc-title" x="56" y="19">FILM</text>
    <use href="#tick" x="-30" y="55" width="11" height="11"/><text class="bullet" x="-6" y="64">Invisible, durable shield</text>
    <use href="#tick" x="-30" y="72.5" width="11" height="11"/><text class="bullet" x="-6" y="81.5">Self-healing technology</text>
    <use href="#tick" x="-30" y="90" width="11" height="11"/><text class="bullet" x="-6" y="99">10-year warranty by QR VONT</text>
  </g>

  <!-- Polishing -->
  <g class="service-card" transform="translate(71,286)">
    <rect class="pill" x="-10" y="-26" width="210" height="52" rx="8"/>
    <g role="img" aria-label="Photo: rotary polisher on a car panel"><circle class="ring" r="34" fill="url(#thumbTone)"/></g>
    <text class="svc-title" x="56" y="8">POLISHING</text>
    <use href="#tick" x="-30" y="55" width="11" height="11"/><text class="bullet" x="-6" y="64">Eliminates scratches, holograms</text>
    <use href="#tick" x="-30" y="72.5" width="11" height="11"/><text class="bullet" x="-6" y="81.5">Revives and protects paint</text>
    <use href="#tick" x="-30" y="90" width="11" height="11"/><text class="bullet" x="-6" y="99">Ensures lasting gloss</text>
    <use href="#tick" x="-30" y="107.5" width="11" height="11"/><text class="bullet" x="-6" y="116.5">Enhances paint life</text>
    <use href="#tick" x="-30" y="125" width="11" height="11"/><text class="bullet" x="-6" y="134">Preserves car's value and beauty</text>
  </g>

  <!-- Dry ice wash -->
  <g class="service-card" transform="translate(374,286)">
    <rect class="pill" x="-10" y="-26" width="210" height="52" rx="8"/>
    <g role="img" aria-label="Photo: dry ice blasting a wheel hub"><circle class="ring" r="34" fill="url(#thumbTone)"/></g>
    <text class="svc-title" x="56" y="-3">DRY ICE</text>
    <text class="svc-title" x="56" y="19">WASH</text>
    <use href="#tick" x="-30" y="55" width="11" height="11"/><text class="bullet" x="-6" y="64">Innovative, waterless method</text>
    <use href="#tick" x="-30" y="72.5" width="11" height="11"/><text class="bullet" x="-6" y="81.5">Safe for all car parts</text>
    <use href="#tick" x="-30" y="90" width="11" height="11"/><text class="bullet" x="-6" y="99">Deep cleans, removes odors</text>
    <use href="#tick" x="-30" y="107.5" width="11" height="11"/><text class="bullet" x="-6" y="116.5">Allergen-free, antibacterial</text>
    <use href="#tick" x="-30" y="125" width="11" height="11"/><text class="bullet" x="-6" y="134">Gentle, effective</text>
    <use href="#tick" x="-30" y="142.5" width="11" height="11"/><text class="bullet" x="-6" y="151.5">Advanced cleaning technology</text>
  </g>

  <!-- Detailing boutique -->
  <g class="service-card" transform="translate(680,286)">
    <rect class="pill" x="-10" y="-26" width="210" height="52" rx="8"/>
    <g role="img" aria-label="Photo: car care products on an orange shelf"><circle class="ring" r="34" fill="url(#thumbTone)"/></g>
    <text class="svc-title" x="56" y="-3">DETAILING</text>
    <text class="svc-title" x="56" y="19">BOUTIQUE</text>
    <use href="#tick" x="-30" y="55" width="11" height="11"/><text class="bullet" x="-6" y="64">Premium brands available</text>
    <use href="#tick" x="-30" y="72.5" width="11" height="11"/><text class="bullet" x="-6" y="81.5">Buy on site during your visit</text>
    <use href="#tick" x="-30" y="90" width="11" height="11"/><text class="bullet" x="-6" y="99">Marble Harbour, Zeb Autos, DRUP Polaro</text>
    <use href="#tick" x="-30" y="107.5" width="11" height="11"/><text class="bullet" x="-6" y="116.5">Essential for at-home car care</text>
    <use href="#tick" x="-30" y="125" width="11" height="11"/><text class="bullet" x="-6" y="134">Perfect for quick touch-ups</text>
  </g>

  <!-- Covering -->
  <g class="service-card" transform="translate(374,488)">
    <rect class="pill" x="-10" y="-26" width="210" height="52" rx="8"/>
    <g role="img" aria-label="Photo: vinyl wrap being fitted to a car"><circle class="ring" r="34" fill="url(#thumbTone)"/></g>
    <text class="svc-title" x="56" y="7">COVERING</text>
    <use href="#tick" x="-30" y="55" width="11" height="11"/><text class="bullet" x="-6" y="64">Personalized vehicle styling</text>
    <use href="#tick" x="-30" y="72.5" width="11" height="11"/><text class="bullet" x="-6" y="81.5">More than 150 colours available</text>
    <use href="#tick" x="-30" y="90" width="11" height="11"/><text class="bullet" x="-6" y="99">Clean cut without using a cutter</text>
    <use href="#tick" x="-30" y="107.5" width="11" height="11"/><text class="bullet" x="-6" y="116.5">High-quality, durable materials</text>
    <use href="#tick" x="-30" y="125" width="11" height="11"/><text class="bullet" x="-6" y="134">Custom designs available</text>
  </g>
</svg>

</body>
</html>
```